Unique E-commerce website needs a FLAT UI design

Looking for creative website designer / company to design a flat ui interface for the main 4 pages.

I SEEK FLAT UI DESIGN ONLY - this means nice, clean and modern design,

As we're dealing with the design of the main pages this will define the overall site design so take a moment or two to think on the audience and create an appealing branding.

Website design must be mobile/ipad friendly.

I've written a detailed design requirements document for those 4 pages.
Please read it carefully and make sure you understand every aspect of it before starting the design process.
You can find a brief intro text and some reference designs that I like to get you started.

This is not a closed concept, I'm open to hear new ideas and ways to improve the UI/UX.

Feel free to ask anything, I'm available most of the day.

I'm looking to build a long term relationship as this is the first phase of the design, I have 1-2 phases to come.

Target Market(s)

Online shoppers age between 18-60 that buy frequently at US merchants

Industry/Entity Type

It Company

Number of Pages Required

4 page

Requirements
Must have
• Flat UI design
• Flat colors
• Modern, clean and easy to follow design
Nice to have
• Original icons for the features page

```html
<!DOCTYPE html>
<html lang="en">
<head>
<meta charset="utf-8">
<title>ParcelNest – Ship it over</title>
<link rel="stylesheet" href="https://fonts.googleapis.com/css2?family=Montserrat:wght@400;500;600;700;800&family=Open+Sans:wght@400;600&display=swap">
<style>
:root{
  --green:#34cf77;
  --green-dark:#27b563;
  --navy:#254659;
  --navy-dark:#1d3a4b;
  --yellow:#f1c40f;
  --yellow-dark:#e0b40a;
  --blue:#3498db;
  --orange:#ec6b3d;
  --white:#ffffff;
  --ink:#2c3e50;
  --muted:#8a9199;
  --card-grey:#ececec;
  --footer:#3a3a3a;
  --footer-text:#a9a9a9;
}
*{box-sizing:border-box;margin:0;padding:0}
html,body{width:1200px;height:2759px;overflow:hidden}
body{font-family:"Montserrat",Arial,sans-serif;color:var(--ink);background:var(--white);position:relative}
section,header,footer{position:absolute;left:0;width:1200px}
.abs{position:absolute}

/* Header */
.site-header{top:0;height:530px;background:var(--green)}
.brand{left:162px;top:62px;font-weight:800;font-size:24px;color:var(--white);letter-spacing:-0.3px;white-space:nowrap}
.lang{left:358px;top:68px;font-size:13px;color:var(--white);font-weight:600;display:flex;align-items:center;gap:7px}
.lang .flag{width:20px;height:13px;background:var(--white);border-radius:2px}
.main-nav{right:150px;top:58px;display:flex;align-items:center;gap:38px;font-size:14px;color:var(--white);font-weight:600;text-transform:uppercase}
.main-nav .calc{width:18px;height:22px;border:3px solid var(--white);border-radius:3px}
.main-nav .signup{border:3px solid var(--white);border-radius:6px;padding:5px 22px}
.main-nav .more{font-size:24px;letter-spacing:2px;line-height:1}
.hero-art{left:480px;top:150px;width:250px;height:150px;border-radius:10px;background:linear-gradient(180deg,#5ddf95,#2fbf6c)}
.hero-title{left:0;top:306px;width:1200px;text-align:center;font-weight:400;font-size:42px;color:var(--white)}
.hero-title svg{vertical-align:-6px;margin:0 8px}
.signup-form{left:355px;top:371px;width:490px;height:54px;background:var(--green-dark);border-radius:4px;padding:7px;display:flex;gap:8px}
.signup-form .field{flex:0 0 154px;background:var(--white);border-radius:3px;font-size:14px;color:#aab;padding:11px 12px;font-family:"Open Sans",Arial,sans-serif}
.signup-form .submit{flex:1;background:var(--blue);color:var(--white);font-weight:700;font-size:14px;text-transform:uppercase;display:flex;align-items:center;justify-content:center;border-radius:3px}

/* How it works */
.how{top:530px;height:491px;background:var(--white)}
.section-title{left:0;width:1200px;top:80px;text-align:center;font-size:27px;color:var(--green-dark);font-weight:500}
.step{top:174px;width:280px;text-align:center}
.step .icon{width:124px;height:124px;border-radius:50%;margin:0 auto}
.step h3{margin-top:24px;font-size:20px;font-weight:600;color:var(--ink)}
.step p{margin-top:10px;font-family:"Open Sans",Arial,sans-serif;font-size:14px;line-height:20px;color:var(--muted)}
.step-1{left:210px}.step-1 .icon{background:var(--yellow)}
.step-2{left:459px}.step-2 .icon{background:var(--orange)}
.step-3{left:707px}.step-3 .icon{background:#dbe9f6}

/* Pricing */
.pricing{top:1021px;height:896px;background:var(--navy)}
.plan{border-radius:6px;text-align:center;overflow:hidden}
.plan h4{font-size:20px;font-weight:700;color:var(--ink);line-height:25px}
.plan ul{list-style:none}
.plan li{font-size:13px;line-height:19px;padding:0 18px;display:flex;align-items:center;justify-content:center;flex-direction:column}
.plan .btn{position:absolute;left:16px;right:16px;height:44px;border-radius:4px;font-size:13px;font-weight:700;text-transform:uppercase;display:flex;align-items:center;justify-content:center}
.plan .note{display:inline-block;width:13px;height:13px;border-radius:50%;background:var(--orange);vertical-align:-2px;margin-left:4px}
.plan-package{left:262px;top:149px;width:207px;height:471px;background:var(--green);color:var(--white)}
.plan-package h4{margin-top:40px}
.plan-package ul{margin-top:18px}
.plan-package li{height:72px;border-top:1px solid rgba(255,255,255,.35)}
.plan-package .btn{bottom:16px;background:var(--white);color:var(--ink)}
.plan-extra{left:491px;top:97px;width:218px;height:546px;background:var(--yellow);color:var(--white)}
.plan-extra h4{margin-top:40px}
.plan-extra ul{margin-top:18px}
.plan-extra li{height:76px;border-top:1px solid rgba(255,255,255,.45)}
.plan-extra .btn{bottom:22px;background:var(--navy);color:var(--white)}
.plan-surcharge{left:720px;top:149px;width:218px;height:471px;background:var(--card-grey);color:#5a6570}
.plan-surcharge h4{margin-top:40px}
.plan-surcharge ul{margin-top:18px}
.plan-surcharge li{height:80px;border-top:1px solid #d2d2d2}
.plan-surcharge .btn{bottom:22px;background:var(--navy);color:var(--white)}
.deal{top:723px;height:91px;width:411px;background:#efefef;display:flex;align-items:center}
.deal-a{left:185px}.deal-b{left:607px}
.deal svg{margin-left:12px;flex:0 0 auto}
.deal p{margin-left:14px;font-size:15px;line-height:21px;color:#444}
.deal p b{font-weight:700}

/* Merchants */
.merchants{top:1917px;height:144px;background:var(--yellow);display:flex;align-items:center;justify-content:center;gap:34px}
.merchants span{font-size:22px;font-weight:700;color:var(--white)}

/* Call to action */
.cta{top:2061px;height:469px}
.cta-photo{left:0;top:0;width:1200px;height:469px;background:linear-gradient(120deg,#e8e4dd 0%,#d8cbb8 45%,#b9895b 75%,#8f6a52 100%)}
.cta-box{left:268px;top:141px;width:670px;height:110px;background:var(--white);text-align:center;padding-top:22px}
.cta-box h2{font-size:43px;font-weight:400;color:var(--ink)}
.cta-box p{font-size:20px;color:var(--ink);margin-top:4px}
.cta-btn{left:461px;top:284px;width:284px;height:50px;background:var(--blue);border-radius:4px;color:var(--white);font-weight:600;font-size:20px;display:flex;align-items:center;justify-content:center;text-transform:uppercase}

/* Footer */
.site-footer{top:2530px;height:229px;background:var(--footer)}
.foot-col{top:52px}
.foot-col h5{font-size:14px;font-weight:600;color:var(--white);margin-bottom:18px}
.foot-col li{list-style:none;font-family:"Open Sans",Arial,sans-serif;font-size:13px;line-height:19px;color:var(--footer-text)}
.col-1{left:163px}.col-2{left:359px}.col-3{left:546px}.col-4{left:723px}
.social{display:flex;gap:10px}
.social span{width:38px;height:38px;border-radius:50%;background:#707070}
</style>
</head>
<body>

<header class="site-header">
  <div class="abs brand">PARCELNEST</div>
  <div class="abs lang"><span class="flag"></span>ENG ▾</div>
  <nav class="abs main-nav">
    <span>Features</span><span>Pricing</span><span>Help</span>
    <span class="calc" aria-label="Calculator"></span>
    <span class="signup">Sign up</span>
    <span class="more">•••</span>
  </nav>
  <div class="abs hero-art" role="img" aria-label="Illustration of an open parcel box on a delivery truck with an hourglass"></div>
  <h1 class="abs hero-title">Fetching home some<svg width="56" height="48" viewBox="0 0 56 48"><path d="M28 46 C10 32 2 24 2 14 A12 12 0 0 1 28 9 A12 12 0 0 1 54 14 C54 24 46 32 28 46Z" fill="#fff"/></svg>?</h1>
  <form class="abs signup-form">
    <span class="field">Email</span>
    <span class="field">Password</span>
    <span class="submit">Create account</span>
  </form>
</header>

<section class="how">
  <h2 class="abs section-title">How it works?</h2>
  <div class="abs step step-1">
    <div class="icon" role="img" aria-label="Icon of a laptop showing a shop front"></div>
    <h3>Ship It Over</h3>
    <p>Lorem ipsum dolor sit amet,<br>consectetur adipiscing elit.<br>Aenean vitae luctus ligula.</p>
  </div>
  <div class="abs step step-2">
    <div class="icon" role="img" aria-label="Icon of a delivery truck"></div>
    <h3>Make Way Home</h3>
    <p>Lorem ipsum dolor sit amet,<br>consectetur adipiscing elit.<br>Aenean vitae luctus ligula.</p>
  </div>
  <div class="abs step step-3">
    <div class="icon" role="img" aria-label="Icon of a map pin with footprints"></div>
    <h3>Track Delivery</h3>
    <p>Lorem ipsum dolor sit amet,<br>consectetur adipiscing elit.<br>Aenean vitae luctus ligula.</p>
  </div>
</section>

<section class="pricing">
  <div class="abs plan plan-package">
    <h4>Package Related</h4>
    <ul>
      <li><span>Package processing <b>$1</b></span></li>
      <li><span>Payment Processing</span><b>4% of shipping costs</b></li>
      <li><span>Package Consolidation</span><span>from <b>$2</b><i class="note"></i></span></li>
      <li><span>Storage <b>$1</b><i class="note"></i></span></li>
    </ul>
    <div class="btn">Sign up for free!</div>
  </div>
  <div class="abs plan plan-extra">
    <h4>Extra Services</h4>
    <ul>
      <li><span>Content photos</span><span>from <b>$2</b><i class="note"></i></span></li>
      <li><span>Repacking <b>$5</b></span></li>
      <li><span>Filling Out</span><span>Customs Form <b>$5</b></span></li>
      <li><span>Express Checkout <b>$5</b></span></li>
      <li><span>Custom Requests <b>$5</b></span></li>
    </ul>
    <div class="btn">Learn more</div>
  </div>
  <div class="abs plan plan-surcharge">
    <h4>Surcharges</h4>
    <ul>
      <li><span>Missing Mailbox</span><span>Number <b>$2</b></span></li>
      <li><span>Heavy Package <b>$10</b><i class="note"></i></span></li>
      <li><span>Return Label</span><span>Processing <b>$5</b></span></li>
    </ul>
    <div class="btn">Learn more</div>
  </div>

  <div class="abs deal deal-a">
    <svg width="112" height="112" viewBox="0 0 112 112">
      <polygon points="56,4 101,30 101,82 56,108 11,82 11,30" fill="#f1c40f" stroke="#fff" stroke-width="4"/>
      <text x="56" y="60" text-anchor="middle" font-family="Montserrat,sans-serif" font-weight="700" font-size="38" fill="#2c3e50">10</text>
      <text x="56" y="82" text-anchor="middle" font-family="Montserrat,sans-serif" font-weight="700" font-size="15" fill="#fff">% OFF</text>
    </svg>
    <p>when you order <b>MORE</b><br>than 1 service!</p>
  </div>
  <div class="abs deal deal-b">
    <svg width="112" height="112" viewBox="0 0 112 112">
      <polygon points="56,4 101,30 101,82 56,108 11,82 11,30" fill="#f1c40f" stroke="#fff" stroke-width="4"/>
      <text x="56" y="60" text-anchor="middle" font-family="Montserrat,sans-serif" font-weight="700" font-size="38" fill="#2c3e50">15</text>
      <text x="56" y="82" text-anchor="middle" font-family="Montserrat,sans-serif" font-weight="700" font-size="15" fill="#fff">% OFF</text>
    </svg>
    <p>when you order <b>EXTRA</b> service<br>for <b>EVERY</b> incoming package!</p>
  </div>
</section>

<section class="merchants">
  <span>Shopwell</span><span>Stridemark</span><span>Bidnook</span><span>Craftly</span><span>Rivermart</span><span>Tinytots</span><span>Denimco</span>
</section>

<section class="cta">
  <div class="abs cta-photo" role="img" aria-label="Photo of a courier handing over a cardboard parcel"></div>
  <div class="abs cta-box">
    <h2>Lorem Ipsum Dolor Sit Amet</h2>
    <p>Blandit Massa Libero ut Maurisea</p>
  </div>
  <div class="abs cta-btn">Get started !</div>
</section>

<footer class="site-footer">
  <div class="abs foot-col col-1"><h5>Overview</h5><ul><li>Features</li><li>Pricing</li><li>Package Calculator</li><li>Store Calculator</li></ul></div>
  <div class="abs foot-col col-2"><h5>Company</h5><ul><li>About Us</li><li>Contacts</li></ul></div>
  <div class="abs foot-col col-3"><h5>Help</h5><ul><li>Shipping</li><li>Pricing &amp; Billing</li><li>Services</li><li>Tutorials</li></ul></div>
  <div class="abs foot-col col-4"><h5>Connect</h5><div class="social"><span></span><span></span><span></span></div></div>
</footer>

</body>
</html>
```